Contemporary Elegant Business Card Design for an International Trade Company in the Wine Industry

We need a new business card design for an international trade company in the wine and winemaking industry. The overall feel of the card should be contemporary, upscale, luxurious and elegant. It should communicate confidence and professionalism. The colors should complementary to our logo design (burgundy, gold, and black).
Inspiration: rich velvet tapestry
The card should include the following information:
Business: Corvelle Trading/Shipping, LLC.
Name: Martin R. Obrastow
Title: CEO
Email: marty@corvelletrading.example
Phone: 555-482-1957
www.corvelletrading.example
Reason: We'd like the designers that we requested some additional designs from to still submit designs. Thank you!
Business
Contact Information for Business Card
Title: CEO
Phone: 555-482-1957
www.corvelletrading.example

```html
<!DOCTYPE html>
<html lang="en">
<head>
<meta charset="utf-8">
<title>Corvelle Trading/Shipping, LLC. — Business Card</title>
<link href="https://fonts.googleapis.com/css2?family=Open+Sans:wght@400;600;700&display=swap" rel="stylesheet">
<style>
  :root {
    --backdrop: #e9e4dc;
    --card-black: #0b0b0b;
    --gold: #e0a94a;
    --gold-deep: #c98f2f;
    --map-light: #e6c27a;
    --map-dark: #a77733;
    --burgundy: #7c1626;
    --burgundy-deep: #5e0f1c;
    --white: #ffffff;
  }
  * { box-sizing: border-box; margin: 0; padding: 0; }
  html, body { width: 1200px; height: 913px; overflow: hidden; }
  body {
    background: var(--backdrop);
    font-family: "Open Sans", Arial, sans-serif;
    position: relative;
  }
  .card {
    position: absolute;
    width: 640px;
    height: 366px;
    background: var(--card-black);
    overflow: hidden;
    box-shadow: 0 10px 28px rgba(0,0,0,.28);
  }
  .card--front { left: 60px; top: 70px; }
  .card--back { left: 500px; top: 490px; }

  .art {
    position: absolute;
    display: block;
  }
  .card--front .art { left: 34px; top: 58px; width: 290px; height: 250px; }
  .card--back .art { left: 175px; top: 48px; width: 290px; height: 270px; }

  .band { position: absolute; }
  .band--gold-thin { left: 372px; top: 196px; width: 268px; height: 34px; background: var(--gold); }
  .band--gold-wide { left: 330px; top: 256px; width: 310px; height: 52px; background: var(--gold); }
  .band--white { left: 0; top: 310px; width: 330px; height: 22px; background: var(--white); }

  .brand {
    position: absolute;
    left: 120px;
    top: 262px;
    font-size: 38px;
    font-weight: 600;
    letter-spacing: 1px;
    color: var(--white);
    line-height: 1;
  }

  .person {
    position: absolute;
    right: 34px;
    top: 28px;
    text-align: right;
    color: var(--gold);
  }
  .person__name {
    font-size: 21px;
    font-weight: 700;
    letter-spacing: 1.5px;
    text-transform: uppercase;
  }
  .person__title { font-size: 12px; font-weight: 400; margin-top: 2px; }

  .contact {
    position: absolute;
    right: 30px;
    top: 112px;
    list-style: none;
    text-align: right;
    color: var(--gold);
    font-size: 14px;
    line-height: 22px;
  }
  .contact li { display: flex; justify-content: flex-end; align-items: center; gap: 8px; }
  .contact svg { width: 12px; height: 12px; fill: none; stroke: var(--gold); stroke-width: 1.6; }
</style>
</head>
<body>

<section class="card card--front" aria-label="Business card front">
  <svg class="art" viewBox="0 0 290 250" role="img" aria-label="Antique world map in gold tones over a burgundy diagonal panel">
    <defs>
      <linearGradient id="mapToneFront" x1="0" y1="0" x2="1" y2="1">
        <stop offset="0" stop-color="var(--map-dark)"/>
        <stop offset=".55" stop-color="var(--map-light)"/>
        <stop offset="1" stop-color="var(--map-dark)"/>
      </linearGradient>
    </defs>
    <rect width="290" height="250" fill="url(#mapToneFront)"/>
    <polygon points="0,250 290,120 290,250" fill="var(--burgundy)"/>
    <polygon points="0,250 0,150 290,120" fill="var(--burgundy-deep)"/>
  </svg>

  <div class="band band--gold-thin"></div>
  <div class="band band--gold-wide"></div>
  <div class="band band--white"></div>

  <div class="brand">CORVELLE</div>

  <div class="person">
    <div class="person__name">Martin R. Obrastow</div>
    <div class="person__title">CEO</div>
  </div>

  <ul class="contact">
    <li>555-482-1957
      <svg viewBox="0 0 12 12"><path d="M2.5 1.5l2 2-1 1.5c.8 1.5 1.7 2.4 3 3l1.5-1 2 2-1.5 1.5C5 10 2 7 1 3z"/></svg>
    </li>
    <li>marty@corvelletrading.example
      <svg viewBox="0 0 12 12"><rect x="1" y="2.5" width="10" height="7"/><path d="M1 2.5l5 4 5-4"/></svg>
    </li>
    <li>www.corvelletrading.example
      <svg viewBox="0 0 12 12"><circle cx="6" cy="6" r="5"/><path d="M1 6h10M6 1c2.5 3 2.5 7 0 10M6 1c-2.5 3-2.5 7 0 10"/></svg>
    </li>
  </ul>
</section>

<section class="card card--back" aria-label="Business card back">
  <svg class="art" viewBox="0 0 290 270" role="img" aria-label="Antique world map in gold tones over a burgundy diagonal panel">
    <defs>
      <linearGradient id="mapToneBack" x1="0" y1="0" x2="1" y2="1">
        <stop offset="0" stop-color="var(--map-dark)"/>
        <stop offset=".55" stop-color="var(--map-light)"/>
        <stop offset="1" stop-color="var(--map-dark)"/>
      </linearGradient>
    </defs>
    <rect width="290" height="270" fill="url(#mapToneBack)"/>
    <polygon points="0,270 0,120 290,110 290,270" fill="var(--burgundy)"/>
  </svg>
</section>

</body>
</html>
```